Home Care App Design

We would like a responsive app design (mobile/web) for an app that will be used by our staff. These need to work display nearly the same for Zentrik and Android. The app tracks caregiver tasks (check-in time, daily client activities, caregiver notes, and check out time) and provides updates to team and family members
Updates

I have added individual or grouped pages with better resolution. please let me know if you have any questions

we did not get enough entries so we increase the budget and have not received any new designer entries

Target Market(s)

professional caregivers and family members

Industry/Entity Type

Home Health Care

Font styles to use
Serif

Requirements
Must have
• We currently have a logo - please use colors or slight variants
• We also will need pop-up designs for informational messages and call to actions (with 1-3 options)
Nice to have
• I have attached a sketch of the app, please use this as a guideline. We are looking for ease of use.
• Please feel free to add design aspects that will make it easy to navigate, select options, or enter notes/messages

```html
<!DOCTYPE html>
<html lang="en">
<head>
<meta charset="utf-8">
<title>Kindwell – Home Care App Screens</title>
<link href="https://fonts.googleapis.com/css2?family=Montserrat:wght@400;500;600;700;800&family=Merriweather:wght@700&display=swap" rel="stylesheet">
<style>
:root{
  --sky:#9dd3e6;
  --white:#ffffff;
  --panel:#f2fafd;
  --navy:#3e6475;
  --ink:#2f4f5c;
  --cyan:#00b8dc;
  --red:#f25a57;
  --green:#1ec73a;
  --line:#2f4f5c;
  --muted:#8fa9b3;
}
*{box-sizing:border-box;margin:0;padding:0}
html,body{width:1200px;height:2707px;overflow:hidden;background:var(--sky)}
body{font-family:"Montserrat",sans-serif;color:var(--ink)}
.stage{position:absolute;left:0;top:0;width:1142px;height:2576px;transform:scale(1.0508);transform-origin:0 0}
.screen{position:absolute;width:436px;height:775px;background:var(--white);overflow:hidden}
.abs{position:absolute}
.center-text{position:absolute;left:0;right:0;text-align:center}

/* brand */
.brand-mark{position:absolute;left:169px;top:189px;width:95px;height:93px;border-radius:8px;background:var(--navy)}
.brand-name{font-family:"Merriweather",serif;font-weight:700;font-size:33px;color:var(--navy);top:295px}

/* login form */
.field{position:absolute;left:105px;width:224px;border-bottom:1.5px solid var(--line);font-size:15px;padding-bottom:5px}
.pill-btn{position:absolute;border-radius:30px;background:var(--cyan);color:var(--white);font-weight:600;display:flex;align-items:center;justify-content:center}
.small-link{font-size:12px;color:var(--ink)}
.small-link u{text-decoration:underline}

/* blurred backdrops */
.backdrop{position:absolute;inset:0;filter:blur(5px);opacity:.75}
.ghost{position:absolute;background:#c9d8de;border-radius:6px}

/* modal */
.modal{position:absolute;background:var(--white);border:2.5px solid var(--navy);border-radius:20px;box-shadow:0 4px 10px rgba(0,0,0,.18)}
.input-pill{position:absolute;border:2px solid var(--navy);border-radius:20px;display:flex;align-items:center;gap:8px;padding-left:12px;font-size:12px;font-style:italic;color:var(--muted)}

/* messages screen */
.app-header{position:absolute;left:0;top:0;width:436px;height:66px;background:var(--navy);color:var(--white);font-size:22px;display:flex;align-items:center;justify-content:center;letter-spacing:.5px}
.burger{position:absolute;right:24px;top:22px;width:25px}
.burger i{display:block;height:3.5px;background:var(--white);border-radius:2px;margin-bottom:5px}
.app-body{position:absolute;left:0;top:66px;width:436px;height:600px;background:var(--panel)}
.tabs{position:absolute;left:12px;top:98px;width:410px;height:40px;border:2px solid var(--navy);border-radius:22px;background:var(--white);display:flex;align-items:center;font-size:13px}
.tab{flex:1;text-align:center;position:relative}
.tab.active{position:absolute;left:-2px;top:-2px;width:105px;height:40px;border-radius:22px;background:var(--cyan);color:var(--white);display:flex;align-items:center;justify-content:center}
.tabs .spacer{width:103px;flex:none}
.badge{position:absolute;top:-12px;right:8px;width:15px;height:15px;border-radius:50%;background:var(--red);color:var(--white);font-size:9px;display:flex;align-items:center;justify-content:center}
.status{position:absolute;top:167px;left:0;right:0;text-align:center;font-size:13px}
.status .chip{display:inline-block;background:var(--navy);color:var(--white);border-radius:4px;padding:1px 7px;margin-left:6px;font-size:12px}
.card{position:absolute;left:28px;width:377px;height:118px;border:2.5px solid var(--navy);border-radius:14px;background:var(--white)}
.card .date{position:absolute;right:14px;top:10px;font-size:11px;border-bottom:1.5px solid var(--cyan)}
.card .pin{position:absolute;left:20px;top:33px}
.card .text{position:absolute;left:65px;top:39px;font-size:17.5px;line-height:21px}
.tabbar{position:absolute;left:0;top:666px;width:436px;height:109px;background:var(--white);border-top:3px solid #dfe7ea}
.nav-item{position:absolute;top:10px;width:100px;text-align:center;font-size:15px;font-weight:500}
.nav-item .icon{height:62px;display:flex;align-items:center;justify-content:center;position:relative}
.msg-circle{width:56px;height:56px;border-radius:50%;background:var(--navy);display:flex;align-items:center;justify-content:center}
.dot{position:absolute;width:10px;height:10px;border-radius:50%;background:var(--red);top:0;right:16px}
.menu{position:absolute;left:308px;top:49px;width:106px;height:100px;background:var(--cyan);border:2px solid var(--navy);border-radius:4px;color:var(--white);font-weight:700;font-size:12.5px;padding:10px 0 0 16px;line-height:28.5px}
</style>
</head>
<body>
<div class="stage">

  <!-- Login -->
  <section class="screen" style="left:94px;top:68px">
    <div class="brand-mark"></div>
    <div class="center-text brand-name">Kindwell</div>
    <div class="field" style="top:355px">User id</div>
    <div class="field" style="top:430px">Password</div>
    <div class="pill-btn" style="left:163px;top:483px;width:107px;height:42px;font-size:15px">LOGIN</div>
    <div class="center-text small-link" style="top:540px">Not a Member Yet? <u>SIGN UP</u></div>
    <div class="center-text small-link" style="top:562px"><u>Forgot Password?</u></div>
  </section>

  <!-- Reset password -->
  <section class="screen" style="left:613px;top:68px">
    <div class="backdrop">
      <div class="brand-mark"></div>
      <div class="ghost" style="left:105px;top:445px;width:224px;height:6px"></div>
      <div class="ghost" style="left:163px;top:490px;width:107px;height:30px;background:var(--cyan)"></div>
      <div class="ghost" style="left:130px;top:540px;width:176px;height:8px"></div>
      <div class="ghost" style="left:163px;top:562px;width:107px;height:8px"></div>
    </div>
    <div class="modal" style="left:68px;top:280px;width:300px;height:149px">
      <div class="center-text" style="top:34px;font-size:12px">Enter your email to reset your password</div>
      <div class="input-pill" style="left:22px;top:57px;width:257px;height:34px">
        <svg width="20" height="14" viewBox="0 0 20 14"><rect x="1" y="1" width="18" height="12" rx="2" fill="none" stroke="#00b8dc" stroke-width="1.5"/><path d="M1 2l9 6 9-6" fill="none" stroke="#00b8dc" stroke-width="1.5"/></svg>
        name123@inbox.test
      </div>
    </div>
    <div class="pill-btn" style="left:166px;top:409px;width:108px;height:37px;font-size:12px">SUBMIT</div>
    <div class="pill-btn" style="left:166px;top:457px;width:108px;height:37px;font-size:12px;background:var(--red)">CANCEL</div>
  </section>

  <!-- Reset sent -->
  <section class="screen" style="left:94px;top:898px">
    <div class="backdrop">
      <div class="brand-mark"></div>
      <div class="ghost" style="left:105px;top:445px;width:224px;height:6px"></div>
      <div class="ghost" style="left:163px;top:485px;width:107px;height:38px;background:var(--cyan);border-radius:20px"></div>
      <div class="ghost" style="left:130px;top:542px;width:176px;height:8px"></div>
      <div class="ghost" style="left:163px;top:566px;width:107px;height:8px"></div>
    </div>
    <div class="modal" style="left:68px;top:280px;width:300px;height:149px">
      <svg class="abs" style="left:128px;top:12px" width="42" height="42" viewBox="0 0 42 42"><path d="M36 17a16 16 0 1 1-6-11" fill="none" stroke="#1ec73a" stroke-width="4" stroke-linecap="round"/><path d="M12 20l8 8 18-19" fill="none" stroke="#1ec73a" stroke-width="4.5" stroke-linecap="round" stroke-linejoin="round"/></svg>
      <div class="center-text" style="top:58px;font-size:16.5px;font-weight:700;color:var(--green)">Password reset request sent</div>
      <div class="center-text" style="top:84px;font-size:12px">we've sent an email to</div>
      <div class="center-text" style="top:102px;font-size:12.5px;font-weight:700">kindwellteam@inbox.test</div>
    </div>
    <div class="pill-btn" style="left:163px;top:409px;width:108px;height:37px;font-size:12px">CONTINUE</div>
  </section>

  <!-- Welcome -->
  <section class="screen" style="left:613px;top:898px;background:var(--panel)">
    <div class="backdrop">
      <div class="ghost" style="left:0;top:0;width:436px;height:66px;background:var(--navy);border-radius:0"></div>
      <div class="ghost" style="left:12px;top:98px;width:410px;height:40px;background:#fff;border:2px solid #cfe;border-radius:22px"></div>
      <div class="ghost" style="left:14px;top:100px;width:100px;height:36px;background:var(--cyan);border-radius:20px"></div>
      <div class="ghost" style="left:205px;top:168px;width:75px;height:14px;background:var(--navy)"></div>
      <div class="ghost" style="left:28px;top:196px;width:377px;height:118px;background:#fff;border:2px solid var(--navy);border-radius:14px"></div>
      <div class="ghost" style="left:28px;top:355px;width:377px;height:118px;background:#fff;border:2px solid var(--navy);border-radius:14px"></div>
      <div class="ghost" style="left:28px;top:513px;width:377px;height:118px;background:#fff;border:2px solid var(--navy);border-radius:14px"></div>
      <div class="ghost" style="left:0;top:666px;width:436px;height:109px;background:#fff;border-radius:0"></div>
      <div class="ghost" style="left:34px;top:685px;width:56px;height:56px;background:var(--navy);border-radius:50%"></div>
    </div>
    <div class="modal" style="left:52px;top:237px;width:337px;height:263px">
      <svg class="abs" style="left:142px;top:16px" width="52" height="46" viewBox="0 0 52 46"><path d="M26 44L5 23C-1 16 2 4 13 3c6 0 10 4 13 8 3-4 7-8 13-8 11 1 14 13 8 20z" fill="#f2524f" stroke="#3e6475" stroke-width="2.5"/></svg>
      <div class="center-text" style="top:70px;font-size:21px;font-weight:800;color:var(--navy)">WELCOME MARCUS!</div>
      <div class="center-text" style="top:98px;font-size:16px;line-height:21px">we are so glad that you<br>joined the Kindwell<br>family!</div>
      <div class="center-text" style="top:166px;font-size:14px">do you want to make a quick tutorial?</div>
      <div class="pill-btn" style="left:79px;top:189px;width:174px;height:33px;font-size:14px;font-weight:700">YES, LET'S GO</div>
      <div class="center-text" style="top:227px;font-size:10.5px;text-decoration:underline">No, i'll do it later</div>
    </div>
  </section>

  <!-- Messages -->
  <section class="screen" style="left:94px;top:1728px">
    <header class="app-header">MESSAGES<div class="burger"><i></i><i></i><i></i></div></header>
    <div class="app-body"></div>
    <nav class="tabs"><span class="tab active">Check in</span><span class="spacer"></span><span class="tab">messages<span class="badge">2</span></span><span class="tab">Check out</span><span class="tab">reminders</span></nav>
    <div class="status">Status <span class="chip">Pending ▾</span></div>
    <article class="card" style="top:196px"><span class="date">18/05/2019</span><svg class="pin" width="38" height="48" viewBox="0 0 38 48"><path d="M19 46C8 33 2 25 2 18a17 17 0 0 1 34 0c0 7-6 15-17 28z" fill="#00b8dc" stroke="#3e6475" stroke-width="2.5"/><circle cx="19" cy="18" r="6" fill="#fff" stroke="#3e6475" stroke-width="2"/></svg><div class="text">check in @nora quinn<br>14 elm Rd, Brookhaven,NY.</div></article>
    <article class="card" style="top:355px"><span class="date">18/05/2019</span><svg class="pin" width="38" height="48" viewBox="0 0 38 48"><path d="M19 46C8 33 2 25 2 18a17 17 0 0 1 34 0c0 7-6 15-17 28z" fill="#00b8dc" stroke="#3e6475" stroke-width="2.5"/><circle cx="19" cy="18" r="6" fill="#fff" stroke="#3e6475" stroke-width="2"/></svg><div class="text">check in @leo quinn<br>14 elm Rd, Brookhaven,NY.</div></article>
    <article class="card" style="top:513px"><span class="date">18/05/2019</span><svg class="pin" width="38" height="48" viewBox="0 0 38 48"><path d="M19 46C8 33 2 25 2 18a17 17 0 0 1 34 0c0 7-6 15-17 28z" fill="#00b8dc" stroke="#3e6475" stroke-width="2.5"/><circle cx="19" cy="18" r="6" fill="#fff" stroke="#3e6475" stroke-width="2"/></svg><div class="text">check in @ada quinn<br>14 elm Rd, Brookhaven,NY.</div></article>
    <footer class="tabbar">
      <div class="nav-item" style="left:12px"><div class="icon"><div class="msg-circle"><svg width="32" height="22" viewBox="0 0 32 22"><rect x="1" y="1" width="30" height="20" rx="2" fill="none" stroke="#fff" stroke-width="2"/><path d="M1 2l15 11L31 2M1 21l11-10M31 21L20 11" fill="none" stroke="#fff" stroke-width="2"/></svg></div><span class="dot"></span></div>Messages</div>
      <div class="nav-item" style="left:122px"><div class="icon"><svg width="36" height="30" viewBox="0 0 36 30"><circle cx="11" cy="7" r="6" fill="#3e6475"/><circle cx="25" cy="7" r="6" fill="#3e6475"/><circle cx="18" cy="14" r="5" fill="#3e6475" stroke="#fff" stroke-width="1.5"/><path d="M1 26c0-7 4-11 10-11s10 4 10 11zM15 26c0-7 4-11 10-11s10 4 10 11z" fill="#3e6475"/><path d="M9 30c0-6 4-10 9-10s9 4 9 10z" fill="#3e6475" stroke="#fff" stroke-width="1.5"/></svg></div>Families</div>
      <div class="nav-item" style="left:217px"><div class="icon"><svg width="38" height="34" viewBox="0 0 38 34" fill="none" stroke="#3e6475" stroke-width="1.8" stroke-linejoin="round"><path d="M3 30L14 19l6-10 8-6 5 6-5 7-9 8z"/><path d="M13 33l9-9M20 9l7 7M24 5l5 6M16 14l5 5"/><path d="M2 20l6-4 3 3"/></svg></div>Team</div>
      <div class="nav-item" style="left:319px"><div class="icon"><svg width="28" height="28" viewBox="0 0 28 28"><circle cx="14" cy="14" r="12" fill="none" stroke="#3e6475" stroke-width="2.5"/><path d="M14 7v7h5" fill="none" stroke="#3e6475" stroke-width="2.5" stroke-linecap="round"/></svg></div>time cards</div>
    </footer>
  </section>

  <!-- Messages with account menu -->
  <section class="screen" style="left:613px;top:1728px">
    <header class="app-header">MESSAGES<div class="burger"><i></i><i></i><i></i></div></header>
    <div class="app-body"></div>
    <nav class="tabs"><span class="tab active">Check in</span><span class="spacer"></span><span class="tab">messages<span class="badge">2</span></span><span class="tab">Check out</span><span class="tab">reminders</span></nav>
    <div class="menu">My Account<br>settings<br>Logout</div>
    <div class="status">Status <span class="chip">Pending ▾</span></div>
    <article class="card" style="top:196px"><span class="date">18/05/2019</span><svg class="pin" width="38" height="48" viewBox="0 0 38 48"><path d="M19 46C8 33 2 25 2 18a17 17 0 0 1 34 0c0 7-6 15-17 28z" fill="#00b8dc" stroke="#3e6475" stroke-width="2.5"/><circle cx="19" cy="18" r="6" fill="#fff" stroke="#3e6475" stroke-width="2"/></svg><div class="text">check in @nora quinn<br>14 elm Rd, Brookhaven,NY.</div></article>
    <article class="card" style="top:355px"><span class="date">18/05/2019</span><svg class="pin" width="38" height="48" viewBox="0 0 38 48"><path d="M19 46C8 33 2 25 2 18a17 17 0 0 1 34 0c0 7-6 15-17 28z" fill="#00b8dc" stroke="#3e6475" stroke-width="2.5"/><circle cx="19" cy="18" r="6" fill="#fff" stroke="#3e6475" stroke-width="2"/></svg><div class="text">check in @leo quinn<br>14 elm Rd, Brookhaven,NY.</div></article>
    <article class="card" style="top:513px"><span class="date">18/05/2019</span><svg class="pin" width="38" height="48" viewBox="0 0 38 48"><path d="M19 46C8 33 2 25 2 18a17 17 0 0 1 34 0c0 7-6 15-17 28z" fill="#00b8dc" stroke="#3e6475" stroke-width="2.5"/><circle cx="19" cy="18" r="6" fill="#fff" stroke="#3e6475" stroke-width="2"/></svg><div class="text">check in @ada quinn<br>14 elm Rd, Brookhaven,NY.</div></article>
    <footer class="tabbar">
      <div class="nav-item" style="left:12px"><div class="icon"><div class="msg-circle"><svg width="32" height="22" viewBox="0 0 32 22"><rect x="1" y="1" width="30" height="20" rx="2" fill="none" stroke="#fff" stroke-width="2"/><path d="M1 2l15 11L31 2M1 21l11-10M31 21L20 11" fill="none" stroke="#fff" stroke-width="2"/></svg></div><span class="dot"></span></div>Messages</div>
      <div class="nav-item" style="left:122px"><div class="icon"><svg width="36" height="30" viewBox="0 0 36 30"><circle cx="11" cy="7" r="6" fill="#3e6475"/><circle cx="25" cy="7" r="6" fill="#3e6475"/><circle cx="18" cy="14" r="5" fill="#3e6475" stroke="#fff" stroke-width="1.5"/><path d="M1 26c0-7 4-11 10-11s10 4 10 11zM15 26c0-7 4-11 10-11s10 4 10 11z" fill="#3e6475"/><path d="M9 30c0-6 4-10 9-10s9 4 9 10z" fill="#3e6475" stroke="#fff" stroke-width="1.5"/></svg></div>Families</div>
      <div class="nav-item" style="left:217px"><div class="icon"><svg width="38" height="34" viewBox="0 0 38 34" fill="none" stroke="#3e6475" stroke-width="1.8" stroke-linejoin="round"><path d="M3 30L14 19l6-10 8-6 5 6-5 7-9 8z"/><path d="M13 33l9-9M20 9l7 7M24 5l5 6M16 14l5 5"/><path d="M2 20l6-4 3 3"/></svg></div>Team</div>
      <div class="nav-item" style="left:319px"><div class="icon"><svg width="28" height="28" viewBox="0 0 28 28"><circle cx="14" cy="14" r="12" fill="none" stroke="#3e6475" stroke-width="2.5"/><path d="M14 7v7h5" fill="none" stroke="#3e6475" stroke-width="2.5" stroke-linecap="round"/></svg></div>time cards</div>
    </footer>
  </section>

</div>
</body>
</html>
```